Business Cards

I'd like help creating business cards with the full logo "Veltrona Capital Partners" on the back of the card (navy background with white writing), and abbreviated logo "VCP" on the front. Would like to list name, title, phone number, email, and website listed on front of card. Would like to keep very simple. Front font Arial or similar.

```html
<!DOCTYPE html>
<html lang="en">
<head>
<meta charset="utf-8">
<title>Veltrona Capital Partners – Business Cards</title>
<link href="https://fonts.googleapis.com/css2?family=Manrope:wght@400;500;700;800&display=swap" rel="stylesheet">
<style>
  :root {
    --navy: #00346d;
    --white: #ffffff;
    --backdrop: #3d3d3d;
  }
  * { margin: 0; padding: 0; box-sizing: border-box; }
  html, body {
    width: 1200px; height: 1200px; overflow: hidden;
    background: var(--backdrop);
    font-family: "Manrope", Arial, sans-serif;
  }
  .card {
    position: absolute;
    left: 233px;
    width: 727px;
    height: 419px;
  }
  .card-front { top: 164px; background: var(--white); color: var(--navy); }
  .card-back { top: 650px; background: var(--navy); color: var(--white); }

  .front-frame {
    position: absolute;
    left: 20px; top: 21px; right: 20px; bottom: 19px;
    border: 13px solid var(--navy);
  }
  .monogram {
    position: absolute;
    left: 58px; top: 100px;
    font-size: 92px; font-weight: 800;
    letter-spacing: 1px;
    line-height: 1;
  }
  .website {
    position: absolute;
    left: 61px; top: 336px;
    font-size: 22px; font-weight: 700;
  }
  .holder-name {
    position: absolute;
    left: 356px; top: 98px;
    font-size: 27px; font-weight: 700;
  }
  .holder-title {
    position: absolute;
    left: 356px; top: 132px;
    font-size: 16px; font-weight: 400;
  }
  .address {
    position: absolute;
    left: 356px; top: 205px;
    font-size: 17.5px; line-height: 24px;
    font-style: normal;
  }
  .contact-list {
    position: absolute;
    left: 356px; top: 282px;
    font-size: 16px; line-height: 20.5px;
    list-style: none;
  }
  .contact-list li { display: flex; }
  .contact-label { width: 55px; }
  .contact-sep { width: 7px; }

  .wordmark {
    position: absolute;
    left: 0; right: 0; top: 150px;
    text-align: center;
    font-weight: 800;
    line-height: 1;
  }
  .wordmark-name {
    display: block;
    font-size: 64px;
    letter-spacing: 2px;
  }
  .wordmark-sub {
    display: block;
    margin-top: 12px;
    font-size: 22px;
    letter-spacing: 13.5px;
    padding-left: 13.5px;
  }
</style>
</head>
<body>
  <section class="card card-front" aria-label="Business card front">
    <div class="front-frame"></div>
    <div class="monogram">VCP</div>
    <div class="website">veltronacp.com</div>
    <h1 class="holder-name">Marcus Ellery</h1>
    <p class="holder-title">Chief Investment Officer and Partner</p>
    <address class="address">2740 West Meridian Avenue<br>Brookhaven, SD 57210</address>
    <ul class="contact-list">
      <li><span class="contact-label">Office</span><span class="contact-sep">:</span><span>877-555-0142</span></li>
      <li><span class="contact-label">Cell</span><span class="contact-sep">:</span><span>214-555-0187</span></li>
      <li><span class="contact-label">Fax</span><span class="contact-sep">:</span><span>469-555-0163</span></li>
      <li><span class="contact-label">Email</span><span class="contact-sep">:</span><span>marcus.ellery@veltronacp.com</span></li>
    </ul>
  </section>

  <section class="card card-back" aria-label="Business card back">
    <div class="wordmark">
      <span class="wordmark-name">VELTRONA</span>
      <span class="wordmark-sub">CAPITAL PARTNERS</span>
    </div>
  </section>
</body>
</html>
```